Hi Designers,

I will need 4 web pages designed. The web page looks like an App (if you click on the logo, or the icon on an iPad, it will take you to the website), but it is still a webpage.

Please check the attachment on this brief to understand what specific pages I need to be designed.

A .PSD (straight-up PhotoShop image) as final deliverable is fine, as long as you give us the exact “web color numbers”.

The design is for desktop and iPad but in a single unified web application, NOT separate web app and (native) iPad app.

Details:

Bright Harbor Policy Systems is developing a browser-based application for use on any mobile device or desktop. The app will be used by corporations to communicate with their employees regarding legal, regulatory and company requirements for conducting business. The app is known as “Workplace Guidance Hub.” When the user clicks on the icon for Workplace Guidance Hub, they will enter a site full of information that a company deems necessary for the employee to do his/her job. There are several content sections within the site, including a login page, training, policies, forms, news feeds and blogs.

The application has been built using Microsoft .NET, and fully supports CSS-type skinning; it uses traditional page layouts. We are seeking a product logo concept (image), a master application/desktop icon (image), as well as a full color scheme/theme/skin design for all areas of the application (header area, body text, menu bar, etc.) in the form of a CSS. The look should be clean, crisp and professional; nothing cartoony or whimsical. It should be easy to read and “airy”.

We have sketched prototypes for the basic application page layout that we can send as a next step of the process.
Updates

Screen shots have been uploaded to this project.  Please use them to guide your design.

Dear designers,

I apologize for the delay in providing feedback. My partners and I will provide feedback in a few days. Thank you for your patience.

Industry/Entity Type

Business

Font styles to use
Other font styles liked:
• see font on screen shots when uploaded

```html
<!DOCTYPE html>
<html lang="en">
<head>
<meta charset="utf-8">
<title>Workplace Guidance Hub – Dashboard</title>
<link rel="stylesheet" href="https://fonts.googleapis.com/css2?family=Open+Sans:ital,wght@0,400;0,600;0,700;1,400&display=swap">
<style>
:root{
  --topbar-1:#3d4043;
  --topbar-2:#232527;
  --topbar-active:#1c1d1f;
  --badge:#e64a2e;
  --page:#f1eee8;
  --sidebar:#f3f8fc;
  --sidebar-line:#d9dee2;
  --ink:#2b2b2b;
  --ink-soft:#5d5d5d;
  --ink-faint:#8a8a8a;
  --icon:#a9adb0;
  --card:#ffffff;
  --row-alt:#ebebeb;
  --head-1:#f7f7f7;
  --head-2:#e6e6e6;
  --accent:#6b3d63;
  --social:#8fa3b3;
  --pill:#3b3b3b;
  --photo-1:#e7b48e;
  --photo-2:#3f8fb0;
}
*{box-sizing:border-box;margin:0;padding:0}
html,body{width:1200px;height:712px;overflow:hidden}
body{font-family:"Open Sans",Arial,sans-serif;background:var(--page);color:var(--ink);position:relative}

/* top bar */
.topbar{position:absolute;left:0;top:0;width:1200px;height:49px;background:linear-gradient(var(--topbar-1),var(--topbar-2));color:#fff;font-size:13px;font-weight:600}
.nav-item{position:absolute;top:0;height:49px;display:flex;align-items:center;gap:9px;padding:0 12px}
.nav-item.active{background:var(--topbar-active)}
.nav-sep{position:absolute;top:14px;width:1px;height:22px;background:#4d5054}
.badge{width:17px;height:17px;border-radius:50%;background:var(--badge);font-size:10px;display:flex;align-items:center;justify-content:center}
.top-search{position:absolute;left:511px;top:12px;width:199px;height:28px;border-radius:6px;background:#1d1e20;display:flex;align-items:center;gap:14px;padding-left:12px;font-size:13px;color:#e5e5e5}
.user{position:absolute;right:14px;top:6px;display:flex;align-items:center;gap:8px;line-height:15px}
.avatar{width:32px;height:32px;border-radius:50%;border:2px solid #ddd;background:linear-gradient(#b58a6e,#6d5648)}

/* sidebar */
.sidebar{position:absolute;left:0;top:49px;width:240px;height:663px;background:var(--sidebar);border-right:1px solid var(--sidebar-line)}
.sidebar h2{font-size:12px;font-weight:700;margin:19px 0 0 14px;color:#222}
.side-search{margin:13px 0 0 10px;width:198px;height:28px;border:2px solid #e2e6ea;border-radius:7px;background:#fff;display:flex;align-items:center;gap:10px;padding-left:10px;font-size:12px;color:#aaa}
.side-nav{list-style:none;margin-top:14px}
.side-nav li{height:52px;border-bottom:1px solid var(--sidebar-line);display:flex;align-items:center;gap:13px;padding-left:11px;font-size:13px;font-weight:600;color:#6a6e72}
.side-nav li:first-child{border-top:1px solid transparent}
.signin{padding:26px 0 0 17px}
.signin h3{font-size:23px;font-weight:400;color:#333}
.signin p{font-size:14.5px;color:#333;margin-top:11px}
.register{margin-top:17px;width:214px;height:38px;border:1px solid #d9dcdf;background:#fff;font-size:13px;color:#666;display:flex;align-items:center;padding-left:5px}
.socials{display:flex;gap:14px;margin-top:19px}
.socials span{width:32px;height:32px;border-radius:50%;background:var(--social)}
.copyright{font-size:11.5px;color:#555;margin-top:16px}

/* section titles */
.section-title{position:absolute;font-size:14px;color:#333;display:flex;align-items:center;gap:7px}
.dots{width:12px;height:8px;display:grid;grid-template-columns:repeat(3,3px);gap:2px}
.dots i{width:3px;height:3px;background:var(--accent)}

/* game card */
.game-card{position:absolute;left:282px;top:121px;width:627px;height:209px;background:var(--card);border-radius:3px;box-shadow:0 1px 3px rgba(0,0,0,.2)}
.card-head{height:29px;background:linear-gradient(var(--head-1),var(--head-2));border-bottom:1px solid #d8d8d8;font-size:12px;font-weight:700;padding:7px 0 0 16px;color:#333}
.photo{position:absolute;left:18px;top:44px;width:108px;height:108px;border-radius:4px;background:linear-gradient(135deg,var(--photo-1),var(--photo-2))}
.card-body{position:absolute;left:153px;top:37px;width:460px}
.card-body h1{font-size:19px;font-weight:400;line-height:29px;color:#333}
.pill{display:inline-block;margin-left:8px;background:var(--pill);color:#fff;font-size:11px;border-radius:3px;padding:0 19px;line-height:19px;vertical-align:2px}
.card-body p{font-size:11.5px;line-height:22px;color:#666;margin-top:6px}
.meta{position:absolute;left:155px;top:175px;display:flex;align-items:center;font-size:11px;font-style:italic;color:#777}
.meta .cell{display:flex;align-items:center;gap:8px;padding-right:20px;margin-right:20px;border-right:1px solid #ddd;height:22px}
.meta .cell:last-of-type{border:none;margin-right:42px}
.meta .mini{width:20px;height:20px;border-radius:50%;background:#dfe6e3;border:2px solid #a6b5ae;margin-right:6px}

/* tabs */
.tabs{position:absolute;left:283px;top:361px;width:626px;height:46px;background:#fff;border:1px solid #d6d6d6}
.tab{position:absolute;top:0;height:44px;display:flex;align-items:center;font-size:12px;font-weight:700}
.tab.answers{left:10px}
.tab.reviews{left:76px;width:130px;background:#ececec;padding-left:32px}
.view-toggle{position:absolute;right:15px;top:10px;display:flex;border:1px solid #c8c8c8;border-radius:3px;overflow:hidden}
.view-toggle span{width:31px;height:26px;display:flex;align-items:center;justify-content:center;background:#fafafa;border-left:1px solid #c8c8c8}
.view-toggle span:first-child{border:none;background:#dedede}

/* data tables */
.data-table{position:absolute;border-collapse:collapse;background:#fff;box-shadow:0 1px 3px rgba(0,0,0,.2)}
.data-table th{height:36px;background:linear-gradient(var(--head-1),var(--head-2));font-weight:600;text-align:left;color:#444;border-bottom:1px solid #d4d4d4}
.data-table tr:nth-child(even) td{background:var(--row-alt)}
.answers-table{left:283px;top:427px;width:626px;font-size:11px}
.answers-table th{font-size:13px;font-weight:400;color:#555}
.answers-table td{height:44.5px;color:#222}
.answers-table .c1{padding-left:29px;width:154px;font-weight:600}
.answers-table .c3{width:87px;font-weight:700;font-size:10.5px}
.caret{display:inline-block;width:0;height:0;border:4px solid transparent;border-top:5px solid #666;margin-left:5px;vertical-align:-3px}
.leader-table{left:953px;top:123px;width:239px;font-size:11px}
.leader-table th{font-size:12.5px;color:#333}
.leader-table td{height:43.6px;font-weight:600;font-size:10px;color:#222}
.leader-table .c1{padding-left:15px;font-weight:400;font-size:11.5px;color:#888;width:90px}
.leader-table th.c1{font-size:12.5px;color:#333;font-weight:600}
.leader-table .c2{width:70px}
</style>
</head>
<body>

<header class="topbar">
  <div class="nav-item active" style="left:28px;width:113px">
    <svg width="16" height="12" viewBox="0 0 16 12"><path d="M1 11a7 7 0 0 1 14 0z" fill="#fff"/><path d="M8 10 11 5" stroke="#232527" stroke-width="1.6"/></svg>
    Home <span class="badge">3</span>
  </div>
  <div class="nav-item" style="left:151px">
    <svg width="13" height="13" viewBox="0 0 13 13" fill="#fff"><rect x="0" y="0" width="13" height="2"/><g><rect x="1" y="4" width="2" height="2"/><rect x="5" y="4" width="2" height="2"/><rect x="9" y="4" width="2" height="2"/><rect x="1" y="8" width="2" height="2"/><rect x="5" y="8" width="2" height="2"/><rect x="9" y="8" width="2" height="2"/></g></svg>
    Menu
  </div>
  <span class="nav-sep" style="left:252px"></span>
  <div class="nav-item" style="left:265px">
    <svg width="14" height="14" viewBox="0 0 14 14"><path d="M6 2H1v11h11V8" fill="none" stroke="#fff" stroke-width="2"/><path d="M5 9 12 2" stroke="#fff" stroke-width="2"/></svg>
    Hcp 360
  </div>
  <span class="nav-sep" style="left:372px"></span>
  <div class="nav-item" style="left:380px">
    <svg width="14" height="14" viewBox="0 0 14 14" fill="#fff"><rect x="1" y="0" width="2" height="14"/><rect x="6" y="0" width="2" height="14"/><rect x="11" y="0" width="2" height="14"/><rect x="0" y="8" width="4" height="2"/><rect x="5" y="3" width="4" height="2"/><rect x="10" y="6" width="4" height="2"/></svg>
    Game
  </div>
  <span class="nav-sep" style="left:485px"></span>
  <div class="top-search">
    <svg width="14" height="14" viewBox="0 0 14 14"><circle cx="5.5" cy="5.5" r="4.5" fill="none" stroke="#777" stroke-width="2"/><path d="M9 9l4 4" stroke="#777" stroke-width="2"/></svg>
    Search...
  </div>
  <div class="user">
    <svg width="26" height="20" viewBox="0 0 26 20" fill="#fff"><rect x="4" y="4" width="6" height="14"/><rect x="11" y="1" width="6" height="17"/><rect x="18" y="7" width="6" height="11"/><rect x="0" y="18" width="26" height="2"/></svg>
    <div>Dana<br>Holt</div>
    <div class="avatar" role="img" aria-label="User profile photo"></div>
  </div>
</header>

<aside class="sidebar">
  <h2>INDUSTRY NEWS</h2>
  <div class="side-search">
    <svg width="14" height="14" viewBox="0 0 14 14"><circle cx="5.5" cy="5.5" r="4.5" fill="none" stroke="#333" stroke-width="2"/><path d="M9 9l4 4" stroke="#333" stroke-width="2.4"/></svg>
    Search...
  </div>
  <ul class="side-nav">
    <li><svg width="30" height="32" viewBox="0 0 30 32" fill="var(--icon)"><circle cx="15" cy="8" r="7"/><path d="M2 31c0-9 6-14 13-14s13 5 13 14z"/></svg>Compliance News</li>
    <li><svg width="30" height="24" viewBox="0 0 30 24" fill="var(--icon)"><ellipse cx="11" cy="9" rx="11" ry="8"/><ellipse cx="20" cy="14" rx="10" ry="7" fill="#c4c7ca"/><path d="M4 15 2 21 9 16z"/></svg>Docementry</li>
    <li><svg width="30" height="30" viewBox="0 0 30 30" fill="var(--icon)"><circle cx="10" cy="13" r="6"/><path d="M0 30c0-7 4-11 10-11s10 4 10 11z"/><ellipse cx="22" cy="6" rx="8" ry="6"/></svg>Compliance Blog</li>
    <li><svg width="30" height="28" viewBox="0 0 30 28" fill="var(--icon)"><circle cx="6" cy="22" r="5"/><rect x="13" y="20" width="13" height="3" rx="1"/><rect x="13" y="15" width="13" height="3" rx="1"/><rect x="15" y="10" width="11" height="3" rx="1"/><rect x="15" y="5" width="11" height="3" rx="1"/><rect x="13" y="25" width="13" height="3" rx="1"/></svg>Relevant Links</li>
    <li><svg width="30" height="26" viewBox="0 0 30 26"><path d="M1 0v25h29" fill="none" stroke="var(--icon)" stroke-width="2"/><path d="M4 20 11 12 17 16 27 5" fill="none" stroke="var(--icon)" stroke-width="2.4"/></svg>Graphics</li>
    <li><svg width="30" height="28" viewBox="0 0 30 28" fill="var(--icon)"><path d="M15 1 0 14h4v14h22V14h4z"/><rect x="12" y="17" width="6" height="11" fill="#e6eaed"/></svg>Home</li>
  </ul>
  <div class="signin">
    <h3>Sign In</h3>
    <p>Just select your favorite social</p>
    <div class="register">Register here</div>
    <div class="socials"><span></span><span></span><span></span><span></span></div>
    <div class="copyright">© &nbsp;2013 All Rights Reserved.</div>
  </div>
</aside>

<div class="section-title" style="left:283px;top:95px"><span class="dots"><i></i><i></i><i></i><i></i><i></i><i></i></span>Compliance Game</div>

<article class="game-card">
  <div class="card-head">CATEGORY ANTI CRUST</div>
  <div class="photo" role="img" aria-label="Photo of two smiling divers in wetsuits"></div>
  <div class="card-body">
    <h1>Vestibulum nec diam massa, eu ullamcorper mi. Fusce ac erat velit, id lacinia. <span class="pill">ALL</span></h1>
    <p>Plusieurs variations de Lorem Ipsum peuvent être trouvées ici ou là, mais la majeure partie d'entre elles a été altérée par l'addition d'humour ou de mots aléatoires qui ne ressemblent pas.</p>
  </div>
  <div class="meta">
    <div class="cell"><svg width="13" height="13" viewBox="0 0 13 13"><rect x="0.5" y="1.5" width="12" height="11" fill="none" stroke="#888"/><rect x="0" y="1" width="13" height="3" fill="#888"/></svg>March 21st , 2013</div>
    <div class="cell"><svg width="14" height="9" viewBox="0 0 14 9"><path d="M0 4.5C3 0 11 0 14 4.5 11 9 3 9 0 4.5z" fill="#777"/><circle cx="7" cy="4.5" r="2" fill="#fff"/></svg>2511</div>
    <div class="cell"><svg width="13" height="12" viewBox="0 0 13 12"><rect x="0" y="5" width="9" height="7" fill="#777"/><path d="M7 5V3a2.5 2.5 0 0 1 5 0v1" fill="none" stroke="#777" stroke-width="1.6"/></svg>Public</div>
    <span class="mini"></span><span class="mini"></span><span class="mini"></span>
  </div>
</article>

<nav class="tabs">
  <div class="tab answers">ANSWERS</div>
  <div class="tab reviews">REVIEWS</div>
  <div class="view-toggle">
    <span><svg width="14" height="11" viewBox="0 0 14 11" fill="#333"><rect width="14" height="2"/><rect y="3" width="14" height="5" fill="none" stroke="#333"/><rect y="9" width="14" height="2"/></svg></span>
    <span><svg width="14" height="11" viewBox="0 0 14 11" fill="#333"><rect width="14" height="2"/><rect y="3" width="14" height="2"/><rect y="6" width="14" height="2"/><rect y="9" width="14" height="2"/></svg></span>
    <span><svg width="13" height="11" viewBox="0 0 13 11" fill="#333"><rect width="3" height="4"/><rect x="5" width="3" height="4"/><rect x="10" width="3" height="4"/><rect y="6" width="3" height="4"/><rect x="5" y="6" width="3" height="4"/><rect x="10" y="6" width="3" height="4"/></svg></span>
  </div>
</nav>

<table class="data-table answers-table">
  <tr><th class="c1">Quantity<span class="caret"></span></th><th>Description<span class="caret"></span></th><th class="c3" style="font-size:13px;font-weight:400">Date<span class="caret"></span></th></tr>
  <tr><td class="c1">7,500</td><td>Lorem ipsum dolor sit amet, consectetuer adipiscing elit, sed diam</td><td class="c3">23 Jul 2013</td></tr>
  <tr><td class="c1">112</td><td>Eodem modo typi, qui nunc</td><td class="c3">10 Aug 2013</td></tr>
  <tr><td class="c1">675</td><td>Typi non habent claritatem insitam; est usus legentis</td><td class="c3">15 Sep 2013</td></tr>
  <tr><td class="c1">12</td><td>Claritas est etiam processus dynamicus, qui sequitur</td><td class="c3">30 Oct 2013</td></tr>
  <tr><td class="c1">4,308</td><td>Nam liber tempor</td><td class="c3">1 Nov 2013</td></tr>
</table>

<div class="section-title" style="left:953px;top:97px"><span class="dots"><i></i><i></i><i></i><i></i><i></i><i></i></span>Leader Board</div>

<table class="data-table leader-table">
  <tr><th class="c1">Board</th><th class="c2">Price</th><th>Date</th></tr>
  <tr><td class="c1">New Events</td><td class="c2">$320</td><td>23 Jul 2013</td></tr>
  <tr><td class="c1">Archive</td><td class="c2">$115</td><td>10 Aug 2013</td></tr>
  <tr><td class="c1">Notes Stories</td><td class="c2">$45</td><td>15 Sep 2013</td></tr>
  <tr><td class="c1">Database</td><td class="c2">$4,200</td><td>30 Oct 2013</td></tr>
  <tr><td class="c1">Schedule</td><td class="c2">$1,050</td><td>1 Nov 2013</td></tr>
  <tr><td class="c1">New Events</td><td class="c2">$320</td><td>23 Jul 2013</td></tr>
  <tr><td class="c1">Archive</td><td class="c2">$115</td><td>10 Aug 2013</td></tr>
  <tr><td class="c1">Notes Stories</td><td class="c2">$45</td><td>15 Sep 2013</td></tr>
  <tr><td class="c1">Database</td><td class="c2">$4,200</td><td>30 Oct 2013</td></tr>
  <tr><td class="c1">Schedule</td><td class="c2">$1,050</td><td>1 Nov 2013</td></tr>
  <tr><td class="c1">New Events</td><td class="c2">$320</td><td>23 Jul 2013</td></tr>
  <tr><td class="c1">Archive</td><td class="c2">$115</td><td>10 Aug 2013</td></tr>
</table>

</body>
</html>
```